Small animal veterinary clinic needs a new web site design

We need a new web site design for Harlowe Veterinary Clinic. The clinic performs medicine, surgery, and wellness care for cats and dogs. We have been in business for over 50 years so we want to project stability, reliability, class, elegance, and professionalism. We also want to convey that we have modern facilities and services and perform high quality medicine.
The current web site has been in place for many years and looks stale but for reference it is at http://www.harlowevc-example.com. We will be re-writing most of the content and looking to add additional pages, videos, downloadable documents (forms, brochures, marketing materials, etc.) The new owners prefer a more classy, modern look. Some vet clinic sites we like are http://pennfrolt.com and http://curaplumtails.com. We like a nice, clean, fresh, interactive interface.
Our new logo is attached. We want the color scheme of the web site to be complementary to the colors in the logo, especially the blue and green. The purple color of the text should just be used for accent. Upon request and if necessary, I can supply the Adobe Illustrator source file for the logo.
We are looking for a set of page designs - a great, eye-catching home page and 2-3 content page layouts we can use to create content pages with our own text and other content. Navigation design is very important as well. Again, we can fill in the content of the navigation links but I would like a nice, easy-to-use, logical navigation design. If you want some content or navigation links to use as reference during your design phase, feel free to pull whatever content or navigation you want from our existing web site. I am not looking for just images, I would like actual page files - HTML, CSS, etc.
Thanks and good luck!
Target Market(s)
We cater to pet owners across a wide age range. Socio-economic status of our customers is middle class and above. We do not target price shoppers.
Industry/Entity Type
Veterinary
Colors
Designer to choose colors to be used in the design.
Requirements
Must have
- Must look professional, clean, and modern. We are looking for simple but elegant design and navigation. 1 home page design, 2-3 content page designs delivered with code (HTML & CSS).
Nice to have
- When HTML/CSS is delivered, it would be awesome if it were mobile ready as well.
Should not have
- Colors that are too bold. Layout that is too complex.

```html
<!DOCTYPE html>
<html lang="en">
<head>
<meta charset="utf-8">
<title>Harlowe Veterinary Clinic</title>
<link href="https://fonts.googleapis.com/css2?family=Arimo:wght@400;700&display=swap" rel="stylesheet">
<style>
  :root{
    --blue:#3d85c6;
    --blue-top:#3b78b3;
    --navy:#0b2d57;
    --navy-frame:#0d2f5b;
    --green:#55b257;
    --green-frame:#4fae52;
    --purple:#4b2a5c;
    --panel:#ececec;
    --text:#555;
    --line:#d6d6d6;
    --white:#fff;
  }
  *{box-sizing:border-box;margin:0;padding:0}
  html,body{width:1200px;height:951px;overflow:hidden}
  body{position:relative;background:var(--white);font-family:"Arimo",Arial,sans-serif;color:var(--text)}
  .band{position:absolute;left:0;top:129px;width:1200px;height:554px;
    background:linear-gradient(180deg,var(--blue-top) 0%,#1e5590 45%,var(--navy) 100%)}
  .band-edge{position:absolute;left:0;top:126px;width:1200px;height:3px;background:#e4e4e4}

  .logo-box{position:absolute;left:55px;top:19px;width:251px;height:230px;background:var(--white);
    border:1px solid #cfcfcf;display:flex;flex-direction:column;align-items:center;justify-content:center;gap:12px}
  .logo-box .mark{width:46px;height:46px;border-radius:50%;background:var(--blue)}
  .logo-box .name{font-size:22px;font-weight:700;color:var(--purple);text-align:center;line-height:1.25}

  .main-nav{position:absolute;left:335px;top:19px;width:810px;height:37px;display:flex;list-style:none}
  .main-nav li{font-size:14px;color:var(--blue);display:flex;align-items:center;justify-content:center;height:37px}
  .main-nav .active{background:var(--blue);color:var(--white);width:155px;border-radius:2px}

  .slider{position:absolute;left:335px;top:65px;width:810px;height:362px;border:7px solid var(--green-frame);border-radius:4px;overflow:hidden}
  .slider .slide{width:100%;height:100%;background:linear-gradient(100deg,#6b4a22 0%,#b98a4a 35%,#d8b27a 60%,#a87a3e 100%)}
  .slider .arrow{position:absolute;top:160px}
  .slider .prev{left:48px}
  .slider .next{right:48px}

  .contact{position:absolute;left:55px;top:296px;color:var(--white)}
  .contact h2{font-size:23px;font-weight:400;margin-bottom:8px}
  .contact p{font-size:14px;font-weight:700;line-height:17.5px}

  .social{position:absolute;left:55px;top:438px;display:flex;gap:31px}
  .social span{width:40px;height:40px;border-radius:5px;background:#e9eef5}

  .cta{position:absolute;left:55px;width:251px;height:39px;background:var(--green);border-radius:3px;
    color:var(--white);font-size:15px;font-weight:700;display:flex;align-items:center;justify-content:center}
  .cta.appointment{top:497px}
  .cta.reservation{top:556px}

  .welcome{position:absolute;left:335px;top:454px;width:810px;height:275px;background:var(--panel);
    border:9px solid var(--navy-frame);border-radius:3px}
  .welcome h1{position:absolute;left:57px;top:62px;font-size:18px;font-weight:400;color:var(--text)}
  .welcome .photo{position:absolute;left:57px;top:80px;width:207px;height:130px;
    background:radial-gradient(circle at 60% 50%,#e8dcc6 0%,#b08f6a 45%,#3a2a1e 100%)}
  .welcome p{position:absolute;left:293px;top:84px;width:440px;font-size:12.5px;line-height:17px;color:var(--text)}
  .welcome a{color:var(--blue);text-decoration:none}

  .card{position:absolute;top:757px;height:220px;border:1px solid var(--blue);background:var(--white)}
  .card h3{height:38px;background:var(--blue);color:var(--white);font-size:14px;font-weight:700;padding:12px 15px}
  .card.services{left:55px;width:345px}
  .card.staff{left:428px;width:344px}
  .card.hours{left:800px;width:345px}

  .service-list{list-style:none;margin:15px 15px 0}
  .service-list li{height:39px;border:1px solid var(--line);margin-bottom:-1px;font-size:13.5px;color:var(--text);
    display:flex;align-items:center;padding-left:15px;gap:7px}

  .staff-row{display:flex;gap:30px;padding:15px 0 0 17px}
  .member{width:84px}
  .member .portrait{width:84px;height:84px;border:1px solid #ccc;padding:3px;background:var(--white)}
  .member .portrait div{width:100%;height:100%;background:linear-gradient(180deg,#c9c2b4 0%,#7b6a58 55%,#2b2724 100%)}
  .member p{font-size:13.5px;line-height:18px;margin-top:5px;color:var(--text)}

  .hours-text{padding:16px 15px 0;font-size:13.5px;line-height:17.5px;color:var(--text)}
  .hours .request{position:absolute;left:15px;top:149px;width:245px;height:45px;background:var(--green);border-radius:3px;
    color:var(--white);font-size:18px;display:flex;align-items:center;justify-content:center}
</style>
</head>
<body>
  <div class="band"></div>
  <div class="band-edge"></div>

  <header class="logo-box">
    <span class="mark"></span>
    <span class="name">Harlowe<br>Veterinary Clinic</span>
  </header>

  <ul class="main-nav">
    <li class="active">Home</li>
    <li style="width:168px">Services</li>
    <li style="width:160px">Our Staff</li>
    <li style="width:152px">Care Guides</li>
    <li style="width:175px">Contact us</li>
  </ul>

  <section class="slider">
    <div class="slide" role="img" aria-label="Sunlit tall grass field with a shepherd dog and a young child"></div>
    <svg class="arrow prev" width="16" height="26" viewBox="0 0 16 26"><path d="M13 2 L3 13 L13 24" fill="none" stroke="rgba(255,255,255,.7)" stroke-width="4"/></svg>
    <svg class="arrow next" width="16" height="26" viewBox="0 0 16 26"><path d="M3 2 L13 13 L3 24" fill="none" stroke="rgba(255,255,255,.7)" stroke-width="4"/></svg>
  </section>

  <aside class="contact">
    <h2>Get In touch With Us</h2>
    <p>Harlowe Veterinary<br>2210 Alder Crest Avenue<br>Marlow Springs, SC 29400<br>Phone: (555) 013-2761<br>Fax: (555) 013-0127</p>
  </aside>

  <div class="social"><span></span><span></span><span></span><span></span></div>

  <div class="cta appointment">Schedule an Appointment Today</div>
  <div class="cta reservation">Make a Reservation Today</div>

  <section class="welcome">
    <h1>Welcome to HARLOWE</h1>
    <div class="photo" role="img" aria-label="Child hugging a pale labrador dog"></div>
    <p>Harlowe Veterinary Clinic is a full-service veterinary medical hospital, located in Marlow Springs, SC. The professional and courteous staff at Harlowe Veterinary Clinic seeks to provide the best possible medical care, surgical care and dental care for their highly-valued…<a href="#">Read more</a></p>
  </section>

  <section class="card services">
    <h3>Our Services</h3>
    <ul class="service-list">
      <li><svg width="11" height="10" viewBox="0 0 11 10"><path d="M5.5 10 L1 5.3 A2.6 2.6 0 0 1 5.5 1.6 A2.6 2.6 0 0 1 10 5.3 Z" fill="#555"/></svg>Bathing</li>
      <li><svg width="11" height="10" viewBox="0 0 11 10"><path d="M5.5 10 L1 5.3 A2.6 2.6 0 0 1 5.5 1.6 A2.6 2.6 0 0 1 10 5.3 Z" fill="#555"/></svg>Day Care</li>
      <li><svg width="11" height="10" viewBox="0 0 11 10"><path d="M5.5 10 L1 5.3 A2.6 2.6 0 0 1 5.5 1.6 A2.6 2.6 0 0 1 10 5.3 Z" fill="#555"/></svg>Dog Boarding</li>
      <li><svg width="11" height="10" viewBox="0 0 11 10"><path d="M5.5 10 L1 5.3 A2.6 2.6 0 0 1 5.5 1.6 A2.6 2.6 0 0 1 10 5.3 Z" fill="#555"/></svg>Fully Stocked Pharmacy</li>
    </ul>
  </section>

  <section class="card staff">
    <h3>Our Staff</h3>
    <div class="staff-row">
      <div class="member"><div class="portrait"><div role="img" aria-label="Portrait of a veterinarian holding a dog"></div></div><p>Marian T.<br>Colfax,<br>D.V.M.</p></div>
      <div class="member"><div class="portrait"><div role="img" aria-label="Portrait of a veterinarian holding a dog"></div></div><p>Owen R.<br>Colfax,<br>D.V.M.</p></div>
      <div class="member"><div class="portrait"><div role="img" aria-label="Portrait of a veterinarian holding a dog"></div></div><p>Lydia P.<br>Brennard,<br>D.V.M.</p></div>
    </div>
  </section>

  <section class="card hours">
    <h3>Opening Hours</h3>
    <div class="hours-text">
      Mon-Fri: 8:00am - 5:30pm<br>Sat: 8:00am - 11:30am<br>Sun: Closed<br>After Hours Emergency: Lowcountry Pet Emergency (555) 014-3372
    </div>
    <div class="request">Request an Appointment &gt;</div>
  </section>
</body>
</html>
```